Electrician Needs A Business Card

I already have a logo and would like a business card to be designed based around this logo the company is called Tolvane Electrical Pty Ltd

The business card will be printed on transparent plastic so I need it to stand out from the crowd. I do not want the card to have anything to do with Electrical on it eg light bulbs, power points etc

I need it to have the following details.

Gareth Pomfrey
Mobile : 0437 519 284
email : gareth@tolvaneelectrical.com.au

If it could incorporate the following onto the bottom of the card
ELECTRICAL - COMMUNICATIONS - AUDIO - VISUAL

```html
<!DOCTYPE html>
<html lang="en">
<head>
<meta charset="utf-8">
<title>Tolvane Electrical – Business Card</title>
<link rel="stylesheet" href="https://fonts.googleapis.com/css2?family=Arimo:wght@400&family=Tinos:wght@400;700&display=swap">
<style>
  :root {
    --page: #ffffff;
    --ink: #1a1a1a;
    --card-black: #0b0b0b;
    --card-white: #ffffff;
    --amber: #f2a531;
    --light-text: #f4f4f4;
    --caption: #333333;
  }
  html, body {
    margin: 0;
    padding: 0;
    width: 964px;
    height: 1200px;
    overflow: hidden;
    background: var(--page);
  }
  .sheet {
    position: relative;
    width: 964px;
    height: 1200px;
  }
  .business-card {
    position: absolute;
    left: 147px;
    top: 373px;
    width: 669px;
    height: 402px;
    background: var(--card-white);
    box-shadow: 2px 3px 8px rgba(0,0,0,0.35);
    overflow: hidden;
  }
  .card-bg {
    position: absolute;
    inset: 0;
  }
  .brand {
    position: absolute;
    left: 38px;
    top: 78px;
    display: flex;
    align-items: center;
    gap: 16px;
  }
  .brand-mark {
    width: 92px;
    height: 92px;
    background: var(--amber);
  }
  .brand-name {
    font-family: "Arimo", Arial, sans-serif;
    font-weight: 400;
    font-size: 40px;
    line-height: 43px;
    color: var(--ink);
    letter-spacing: -0.5px;
  }
  .services {
    position: absolute;
    left: 355px;
    top: 124px;
    margin: 0;
    padding: 0;
    list-style: none;
    font-family: "Tinos", "Times New Roman", serif;
    font-weight: 700;
    font-size: 21px;
    line-height: 22px;
    color: var(--amber);
    letter-spacing: 0.3px;
  }
  .services .arrow {
    font-size: 15px;
    vertical-align: 2px;
    margin-right: 4px;
  }
  .contact {
    position: absolute;
    left: 0;
    right: 0;
    top: 268px;
    text-align: center;
    font-family: "Tinos", "Times New Roman", serif;
    color: var(--light-text);
  }
  .contact-name {
    font-weight: 700;
    font-size: 28px;
    line-height: 38px;
  }
  .contact-line {
    font-weight: 400;
    font-size: 32px;
    line-height: 46px;
  }
  .caption {
    position: absolute;
    left: 0;
    right: 0;
    top: 1128px;
    text-align: center;
    font-family: "Arimo", Arial, sans-serif;
    font-size: 13px;
    line-height: 16px;
    color: var(--caption);
  }
</style>
</head>
<body>
  <div class="sheet">
    <section class="business-card">
      <svg class="card-bg" width="669" height="402" viewBox="0 0 669 402" aria-hidden="true">
        <polygon points="342,0 669,0 669,402 0,402 0,388 342,187" fill="var(--card-black)"/>
      </svg>

      <div class="brand">
        <div class="brand-mark"></div>
        <div class="brand-name">Tolvane<br>Electrical</div>
      </div>

      <ul class="services">
        <li><span class="arrow">►</span>ELECTRICAL</li>
        <li><span class="arrow">►</span>COMMUNICATIONS</li>
        <li><span class="arrow">►</span>AUDIO <span class="arrow">►</span>VISUAL</li>
      </ul>

      <div class="contact">
        <div class="contact-name">Gareth Pomfrey</div>
        <div class="contact-line">Mobile : 0437 519 284</div>
        <div class="contact-line">gareth@tolvaneelectrical.com.au</div>
      </div>
    </section>

    <div class="caption">TolvaneElectrical-BC<br>Single-sided Business Card Design</div>
  </div>
</body>
</html>
```